High Quality fast food restaurant - Tomanyo

Tomanyo is a fast food company with its target's focused on logistic, simplicity, high quality, freshness and modern.

We need a web design where the customers can get a complete idea of our high quality completeness, we want to take fast food to a new upper level.

We would like to see the colours of wood and metal. Pictures have been attached of our local.

We would like to have something in similar to: http://www.qpz.example/
Updates

Images for the food we are going to sell can be found here: http://shrt.example/uWQa7

It will be the images with rice, french fries or pita bread.

Target Market(s)

The fast food eating people between sloppy food and restaurant level.

Industry/Entity Type

Fast Food Restaurant

Requirements
Should not have
• No Flash or Java

```html
<!DOCTYPE html>
<html lang="en">
<head>
<meta charset="utf-8">
<title>Tomanyo – High quality fastfood</title>
<link href="https://fonts.googleapis.com/css2?family=Alfa+Slab+One&family=Arimo&family=Libre+Baskerville:wght@700&family=Open+Sans&family=Roboto+Condensed:wght@300&display=swap" rel="stylesheet">
<style>
  :root {
    --black: #000000;
    --white: #ffffff;
    --ink: #111111;
    --wood-light: #e7b887;
    --wood-mid: #d9a574;
    --wood-dark: #c98f5c;
    --footer: #3a2a1c;
    --footer-text: #e6d6c2;
    --hero-shade: rgba(40, 10, 5, 0.72);
    --rule: #3b2a1a;
  }
  * { box-sizing: border-box; margin: 0; padding: 0; }
  html, body { width: 1186px; height: 1200px; overflow: hidden; background: var(--black); }
  .page { position: relative; width: 1186px; height: 1200px; overflow: hidden; font-family: "Open Sans", sans-serif; }

  .hero-photo {
    position: absolute; left: 0; top: 0; width: 1186px; height: 675px;
    background:
      radial-gradient(ellipse 480px 280px at 730px 400px, #c9793e 0%, #8a3f1f 45%, rgba(0,0,0,0) 80%),
      linear-gradient(180deg, #000 0%, #0d0705 25%, #3a2014 60%, #a86b4a 100%);
  }
  .hero-rule { position: absolute; left: 0; top: 675px; width: 1186px; height: 4px; background: var(--black); }

  .brand { position: absolute; left: 162px; top: 16px; color: var(--white); }
  .brand-name { font-family: "Alfa Slab One", serif; font-size: 62px; line-height: 70px; letter-spacing: 1px; }
  .brand-tagline { font-family: "Alfa Slab One", serif; font-size: 21px; line-height: 24px; margin-left: 50px; }

  .search { position: absolute; left: 876px; top: 9px; width: 162px; height: 19px; background: var(--white); border: 1px solid #999; }
  .search span { position: absolute; left: 4px; top: 1px; font: italic 11px "Arimo", sans-serif; color: #888; }
  .search svg { position: absolute; right: 3px; top: 2px; }

  .main-nav {
    position: absolute; left: 561px; top: 37px; width: 477px; height: 42px;
    background: var(--white); border-radius: 7px;
    display: flex; align-items: center; justify-content: center; gap: 0;
    font-family: "Roboto Condensed", sans-serif; font-weight: 300; font-size: 17px; color: var(--ink);
  }
  .main-nav a { color: var(--ink); text-decoration: none; }
  .main-nav .sep { margin: 0 22px; }

  .hero-panel { position: absolute; left: 162px; top: 239px; width: 488px; height: 232px; background: var(--hero-shade); }
  .hero-panel p {
    position: absolute; left: 28px; top: 46px; width: 450px;
    font-family: "Libre Baskerville", serif; font-weight: 700; font-size: 26px; line-height: 46px;
    color: var(--white); letter-spacing: 0.5px;
  }

  .wood {
    position: absolute; left: 0; top: 679px; width: 1186px; height: 521px;
    background: repeating-linear-gradient(90deg, var(--wood-light) 0px, var(--wood-mid) 7px, var(--wood-light) 13px, var(--wood-dark) 17px, var(--wood-light) 24px);
  }

  .feature-photo {
    position: absolute; left: 148px; top: 690px; width: 603px; height: 278px;
    background: linear-gradient(120deg, #cfe1ea 0%, #f1eee8 35%, #d9b48a 55%, #e46a4e 80%, #eef0f0 100%);
  }
  .welcome { position: absolute; left: 162px; top: 975px; width: 590px; }
  .welcome h1 { font-family: "Alfa Slab One", serif; font-weight: 400; font-size: 20px; line-height: 24px; color: var(--ink); }
  .welcome p { font-family: "Arimo", sans-serif; font-size: 13px; line-height: 15.8px; color: var(--ink); margin: 1px 0 15px 9px; }

  .read-more { position: absolute; font-family: "Arimo", sans-serif; font-size: 13.5px; color: var(--ink); text-decoration: none; }

  .specials { position: absolute; left: 763px; top: 684px; width: 268px; }
  .specials h2 { font-family: "Alfa Slab One", serif; font-weight: 400; font-size: 20px; line-height: 28px; color: var(--ink); margin-left: 6px; }
  .special { position: relative; height: 99px; border-bottom: 1px dashed var(--rule); }
  .special:last-child { border-bottom: none; }
  .special-thumb { position: absolute; left: 6px; top: 4px; width: 93px; height: 80px; }
  .special-text { position: absolute; left: 108px; top: 0; width: 165px; }
  .special-text h3 { font-weight: 400; font-size: 14px; line-height: 19px; color: var(--ink); }
  .special-text p { font-size: 11.3px; line-height: 16.6px; color: var(--ink); }

  .site-footer { position: absolute; left: 148px; top: 1144px; width: 890px; height: 56px; background: var(--footer); text-align: center; color: var(--footer-text); font-size: 12px; }
  .footer-nav { margin-top: 6px; }
  .footer-nav a { color: var(--footer-text); text-decoration: none; }
  .footer-nav .sep { margin: 0 16px; }
  .copyright { margin-top: 7px; }
</style>
</head>
<body>
<div class="page">
  <div class="hero-photo" role="img" aria-label="Close-up photograph of a sesame burger with cheese, tomato, lettuce, onion rings and fries on a dark background"></div>
  <div class="hero-rule"></div>

  <header>
    <div class="brand">
      <div class="brand-name">TOMANYO</div>
      <div class="brand-tagline">High quality fastfood</div>
    </div>
    <div class="search">
      <span>Search here...</span>
      <svg width="14" height="14" viewBox="0 0 14 14" aria-hidden="true">
        <circle cx="5.5" cy="5.5" r="4" fill="none" stroke="#555" stroke-width="1.6"/>
        <line x1="8.5" y1="8.5" x2="13" y2="13" stroke="#555" stroke-width="2"/>
      </svg>
    </div>
    <nav class="main-nav">
      <a href="#">Home</a><span class="sep">|</span>
      <a href="#">Menu</a><span class="sep">|</span>
      <a href="#">About us</a><span class="sep">|</span>
      <a href="#">Contac t us</a><span class="sep">|</span>
      <a href="#">Site Map</a>
    </nav>
  </header>

  <div class="hero-panel">
    <p>Lorem Ipsum is simply dummy text of the printing and typesetting industry.</p>
  </div>

  <div class="wood"></div>

  <main>
    <div class="feature-photo" role="img" aria-label="Photograph of grilled pita bread filled with sliced meat and sauce, with tomato, onion and parsley on a white plate"></div>
    <section class="welcome">
      <h1>Wel come to our site</h1>
      <p>Lorem Ipsum is simply dummy text of the printing and typesetting industry. Lorem Ipsum has been the industry's standard dummy text ever since the 1500s, when an unknown printer took a galley of type and scrambled it to make a type specimen book.</p>
      <p>Lorem Ipsum is simply dummy text of the printing and typesetting industry. Lorem Ipsum has been the industry's standard dummy text ever since the 1500s, when an unknown printer took a galley of type and scrambled it to make a type specimen book.</p>
    </section>
    <a class="read-more" href="#" style="left:665px; top:1120px;">Read More...</a>

    <aside class="specials">
      <h2>Today Specials</h2>
      <div class="special">
        <div class="special-thumb" role="img" aria-label="Photograph of a platter of stuffed vine leaves with lemon and bread" style="background:linear-gradient(135deg,#6b5a3a,#c9a46a,#b8402a);"></div>
        <div class="special-text"><h3>Lorem ipsum dolor</h3><p>Lorem Ipsum is simply dummy text of the printing and typesetting industry.</p></div>
      </div>
      <div class="special">
        <div class="special-thumb" role="img" aria-label="Photograph of a bowl of red stew with yogurt" style="background:linear-gradient(135deg,#8a7a5a,#e8e4dc,#c23a22);"></div>
        <div class="special-text"><h3>Lorem ipsum dolor</h3><p>Lorem Ipsum is simply dummy text of the printing and typesetting industry.</p></div>
      </div>
      <div class="special">
        <div class="special-thumb" role="img" aria-label="Photograph of a plate with tomato, onion rings and grilled vegetables" style="background:linear-gradient(135deg,#f4f2ee,#c8c0b0,#b8322a);"></div>
        <div class="special-text"><h3>Lorem ipsum dolor</h3><p>Lorem Ipsum is simply dummy text of the printing and typesetting industry.</p></div>
      </div>
      <div class="special">
        <div class="special-thumb" role="img" aria-label="Photograph of onions cooking in a pan" style="background:linear-gradient(135deg,#3a2a2a,#8a6a6a,#4a3434);"></div>
        <div class="special-text"><h3>Lorem ipsum dolor</h3><p>Lorem Ipsum is simply dummy text of the printing and typesetting industry.</p></div>
      </div>
    </aside>
    <a class="read-more" href="#" style="left:952px; top:1120px;">Read more...</a>
  </main>

  <footer class="site-footer">
    <nav class="footer-nav">
      <a href="#">Home</a><span class="sep">|</span>
      <a href="#">Menu</a><span class="sep">|</span>
      <a href="#">About us</a><span class="sep">|</span>
      <a href="#">Contac t us</a><span class="sep">|</span>
      <a href="#">Site Map</a>
    </nav>
    <div class="copyright">© 2013 Tomanyo High quality fastfood. All rights reserved.</div>
  </footer>
</div>
</body>
</html>
```